Powerpoint design for european B2B business

We need a Powerpoint design for a newly established IT company with a B2B focus. We want to develop management information systems that help managers communicate goals into their organization and analyze their organizational activities and performance.

We defined the attached color scale, please relate your design to these colors.

The design should be simple and straight, serious and professional and leave enough space for the content ... :-)

Target Market(s)

B2B, companies larger than 200 employees

Industry/Entity Type

Business

Font styles to use
Sans Serif

Requirements
Should not have
• too playful design, clipart style

```html
<!DOCTYPE html>
<html lang="en">
<head>
<meta charset="utf-8">
<title>Transition Page</title>
<link rel="stylesheet" href="https://fonts.googleapis.com/css2?family=Questrial&family=Open+Sans:wght@700&display=swap">
<style>
  :root {
    --stage: #c8c8c8;
    --footer-bg: #f4f4f4;
    --band-green: #89bd9a;
    --rule-white: #ffffff;
    --ink-white: #ffffff;
    --ink-navy: #3b5d8c;
    --brand-navy: #25476b;
    --photo-dark: #0c1626;
    --photo-mid: #1f3f6e;
    --photo-blue: #3a7fc4;
  }
  * { margin: 0; padding: 0; box-sizing: border-box; }
  html, body { width: 1200px; height: 1039px; overflow: hidden; background: var(--stage); }
  .slide {
    position: absolute; left: 111px; top: 127px;
    width: 967px; height: 724px;
    background: var(--footer-bg);
    font-family: "Questrial", "Century Gothic", sans-serif;
  }
  .hero {
    position: absolute; left: 0; top: 0; width: 967px; height: 665px;
    background:
      radial-gradient(ellipse 60% 45% at 60% 50%, rgba(70,140,210,0.55), transparent 70%),
      radial-gradient(ellipse 40% 35% at 25% 40%, rgba(180,200,225,0.35), transparent 70%),
      linear-gradient(180deg, var(--photo-dark) 0%, var(--photo-mid) 45%, #2a4f80 65%, var(--photo-dark) 100%);
  }
  .hero-shade {
    position: absolute; left: 0; top: 0; width: 345px; height: 202px;
    background: rgba(5, 12, 25, 0.45);
  }
  .title-band {
    position: absolute; left: 0; top: 74px; width: 824px; height: 104px;
    background: var(--band-green);
    border-top: 3px solid var(--rule-white);
    border-bottom: 3px solid var(--rule-white);
  }
  .title {
    position: absolute; left: 74px; top: 24px;
    font-size: 43px; font-weight: 400; color: var(--ink-white);
    letter-spacing: 0.5px; line-height: 1;
  }
  .title strong { font-family: "Open Sans", "Century Gothic", sans-serif; font-weight: 700; }
  .intro {
    position: absolute; left: 66px; top: 540px; width: 823px;
    font-size: 17.5px; line-height: 27px; color: var(--ink-white);
    text-align: justify; hyphens: auto;
  }
  .footer {
    position: absolute; left: 0; top: 665px; width: 967px; height: 59px;
    background: var(--footer-bg);
  }
  .page-number {
    position: absolute; left: 74px; top: 20px;
    font-size: 17px; color: var(--ink-navy);
  }
  .brand {
    position: absolute; right: 68px; top: 12px;
    font-size: 29px; color: var(--brand-navy); letter-spacing: -0.5px;
  }
</style>
</head>
<body>
  <section class="slide">
    <div class="hero" role="img" aria-label="Photo of business papers with blue bar charts, glasses, a pen and a tablet on a desk"></div>
    <div class="hero-shade"></div>
    <div class="title-band">
      <h1 class="title">TRANSITION <strong>PAGE</strong></h1>
    </div>
    <p class="intro">Lorem ipsum dolor sit amet, consectetur adipiscing elit, sed do eiusmod tempor incididunt ut labore et dolore magna aliqua. Ut enim ad minim veniam, quis nostrud exercitation ullamco laboris nisi ut aliquip ex ea commodo consequat.</p>
    <footer class="footer">
      <span class="page-number">Page 3</span>
      <span class="brand">Velmora</span>
    </footer>
  </section>
</body>
</html>
```